120ml Jar Label — Masculine Cosmetic Foot Balm for Cracked, Hardworking Heels

We need a print-ready wraparound label for a 120ml jar — a brown/amber glass jar with a black metal screw lid (file photo attached).

--DO NOT PUT A BARCODE ON THE LABEL PLEASE--
**PLEASE READ "PLAN HUDDLE PROJECT BRIEF FINAL.MD" IN ATTACHED FILES IF YOU ARE SUBMITTING A DESIGN.**

The label is 190mm wide × 40mm high.
We need files to be in an .ai format with a 2mm bleed at the end.
Social media handle: @bramblekeepnz (facebook, instagram and tiktok)

Bramble Keep is a New Zealand foot-care brand making practical, no-nonsense products for hardworking men whose jobs wreck their feet. Our flagship product, Ridge Mender Balm, helps fix thick, cracked, hardworking skin.

Brand color scheme and overview is all in the brief file. You may add some brand aligned colors outside of the specified hex codes as you see fit to make a great design. Feel free to remove the "Bramble Keep" text from the logo so Bramble Keep is not doubled up on the front of the label

The tone we want: direct, rugged, and credible — like a workwear brand, not a spa brand. Most cracked-heel products on the market lean soft and feminine; we want to stand apart by looking like a serious fix for a real problem, made in New Zealand.

Full legal requirements for New Zealand cosmetic labelling (ingredients, directions, net contents, origin, etc.) are listed in the attached brief document — these are non-negotiable and must stay legible.

Please see the label attached "Label spacing guide" for this project's rough spacing guide. This label is the same size and sits well on the jar. This label doesn't need to be spaced quite as much as the Verin Label

I want to run the design for a week - I feel 7 days is a good amount of time for designers to see the work, digest the brief and create something remarkable and memorable for Bramble Keep.

Target Market(s)

Working men in New Zealand whose jobs or lifestyle put heavy wear on their feet — tradies, farmers, hospital/shift workers, hunters, and outdoors people. Practical, value-driven buyers rather than luxury skincare shoppers.

Industry/Entity Type

Beauty / Health & Wellness / Cosmetics

Font styles to use
Sans Serif
Other font styles liked:
• Montserrat (bold, headings), Inter (regular, body)

Colors
00AB8E
00BBA5
67D7C9
C6EFE9
E9F9F6
FFC000
F8CF3A
FAE287
FDF2CF
FEFAEE

Requirements
Must have
• All NZ cosmetic labelling requirements from the attached brief (product name, tag line, net contents, ingredients, directions, storage, made in NZ) — legible and complete, not omitted for aesthetics Fits 190mm × 40mm wraparound format for a 120ml brown jar with black lid Uses our existing brand colors: Deep Olive #3C4A34, Bone White #F4EFE6, Terracotta Clay #C1683D, and Warm Grey #4A4540 (exact palette in attached brief) Uses Montserrat (headings) and Inter (body) or close equivalents Incorporates our existing shield-and-wing logo (attached) Brand name and product name clearly readable from a normal shelf/bathroom-cabinet distance
Nice to have
• A style that could extend into a hero/product photo later, similar to the NZ-hills-backdrop look on our website (screenshot attached) — not required for the label itself, just good to keep in mind Original icon work (e.g. a small soak/apply/sock icon set) if it fits the rugged brand feel A design that could work as a small back-label/wraparound split if the front can't fit everything at a readable size
Should not have
• No pastel colors, floral motifs, or delicate script fonts — this should never look like spa/luxury skincare. Don't introduce new brand colors outside the palette provided other than black.

```html
<!DOCTYPE html>
<html lang="en">
<head>
<meta charset="utf-8">
<title>Bramble Keep NZ — Ridge Mender Balm Label</title>
<link href="https://fonts.googleapis.com/css2?family=Montserrat:wght@400;500;600;700;800;900&display=swap" rel="stylesheet">
<style>
  :root {
    --backdrop: #d6d6d6;
    --bone: #f4efe6;
    --terracotta: #c1683d;
    --band-dark: #3d3530;
    --ink: #1c1c1c;
    --wordmark: #3a3a3a;
    --title: #ece8e2;
    --pill: #5c5653;
    --pill-text: #eeeae4;
    --sky-top: #b9cbe0;
    --sky-mid: #dfe6ee;
    --snow: #eef1f4;
    --rock: #8b8d93;
    --ridge: #6d5a4c;
  }
  * { box-sizing: border-box; margin: 0; padding: 0; }
  html, body {
    width: 1200px; height: 849px; overflow: hidden;
    background: var(--backdrop);
    font-family: "Montserrat", sans-serif;
  }
  .label {
    position: absolute; left: 77px; top: 305px;
    width: 1046px; height: 239px;
    background: var(--bone);
    overflow: hidden;
  }
  .scenery {
    position: absolute; left: 0; top: 11px; width: 100%; height: 116px;
    background:
      linear-gradient(180deg, var(--sky-top) 0%, var(--sky-mid) 38%, var(--snow) 55%, var(--rock) 85%, var(--ridge) 100%);
  }
  .rule { position: absolute; left: 0; width: 100%; height: 3px; background: var(--terracotta); }
  .rule--upper { top: 127px; }
  .rule--lower { top: 227px; }
  .base-band {
    position: absolute; left: 0; top: 130px; width: 100%; height: 97px;
    background: var(--band-dark);
  }
  .info { position: absolute; color: var(--ink); font-size: 9.6px; line-height: 9.8px; }
  .info strong { font-weight: 700; font-size: 11.5px; }
  .info--directions { left: 17px; top: 22px; width: 285px; }
  .info--ingredients { left: 17px; top: 62px; width: 275px; }
  .info--storage { left: 829px; top: 93px; width: 200px; }

  .brand-mark {
    position: absolute; left: 493px; top: 3px;
    width: 60px; height: 60px; border-radius: 50%;
    background: var(--band-dark);
  }
  .brand-name {
    position: absolute; left: 373px; top: 77px; width: 300px;
    text-align: center; color: var(--wordmark);
    font-weight: 800; font-size: 27px; line-height: 25px; letter-spacing: 0.5px;
  }
  .brand-name span { display: block; font-size: 16px; line-height: 18px; }

  .product-name {
    position: absolute; left: 273px; top: 138px; width: 500px;
    text-align: center; color: var(--title);
    font-weight: 800; font-size: 35px; line-height: 36px; letter-spacing: -0.3px;
  }
  .tagline {
    position: absolute; left: 418px; top: 179px; width: 208px; height: 20px;
    border-radius: 10px; background: var(--pill);
    color: var(--pill-text); font-weight: 500; font-size: 14px; line-height: 20px; text-align: center;
  }
  .origin {
    position: absolute; left: 373px; top: 205px; width: 300px;
    text-align: center; color: var(--terracotta);
    font-weight: 700; font-size: 11px; letter-spacing: 0.6px;
  }
  .social-handle {
    position: absolute; left: 856px; top: 141px;
    color: #ffffff; font-weight: 600; font-size: 10px;
  }
  .batch-box {
    position: absolute; left: 854px; top: 161px; width: 133px; height: 56px;
    background: #ffffff;
  }
  .net-contents {
    position: absolute; left: 1010px; top: 183px;
    transform: translate(-50%, -50%) rotate(-90deg);
    color: #ffffff; font-weight: 700; font-size: 21px; letter-spacing: 0.5px; white-space: nowrap;
  }
  .badges { position: absolute; left: 0; top: 0; width: 1046px; height: 239px; }
  .badge-ring { fill: var(--terracotta); }
  .badge-inner { fill: none; stroke: #ffffff; stroke-width: 1.2; }
  .badge-caption { font-family: "Montserrat", sans-serif; font-weight: 700; font-size: 6.4px; letter-spacing: 1.3px; }
  .badge-caption--light { fill: #ffffff; }
  .badge-caption--dark { fill: var(--ink); }
</style>
</head>
<body>
  <div class="label">
    <div class="scenery" role="img" aria-label="Snow-capped New Zealand mountain range under a pale blue sky"></div>
    <div class="rule rule--upper"></div>
    <div class="base-band"></div>
    <div class="rule rule--lower"></div>

    <p class="info info--directions"><strong>Directions:</strong> Apply generously to clean, dry feet, focusing on heels and thick or cracked areas. For cracked heels, wear our moisture-locking socks overnight. Use daily.</p>
    <p class="info info--ingredients"><strong>Ingredients:</strong> Shea Butter, Beef Tallow, Beeswax, Grape Seed Oil, Vegetable Glycerin, Lanolin, Panthenol, Glucono-lactone &amp; Sodium Benzoate, Manuka Honey, Allantoin, Vitamin E, Tea Tree Essential Oil, Lemon Myrtle Essential Oil, Rosemary Oleoresin Extract</p>
    <p class="info info--storage"><strong>Storage:</strong> Keep out of direct sunlight. Best used within six months of opening.</p>

    <div class="brand-mark"></div>
    <p class="brand-name">BRAMBLE KEEP<span>NZ</span></p>

    <h1 class="product-name">Ridge Mender Balm</h1>
    <p class="tagline">For Hardworking Soles</p>
    <p class="origin">Made in New Zealand</p>

    <p class="social-handle">@bramblekeepnz</p>
    <div class="batch-box"></div>
    <p class="net-contents">120ML</p>

    <svg class="badges" viewBox="0 0 1046 239" xmlns="http://www.w3.org/2000/svg">
      <defs>
        <path id="arc-a" d="M 37.6 197.5 A 35 35 0 1 1 98.4 197.5"/>
        <path id="arc-b" d="M 122.6 197.5 A 35 35 0 1 1 183.4 197.5"/>
        <path id="arc-c" d="M 206.6 197.5 A 35 35 0 1 1 267.4 197.5"/>
        <path id="arc-d" d="M 825.7 64 A 31 31 0 1 1 878.3 64"/>
        <path id="arc-e" d="M 891.7 64 A 31 31 0 1 1 944.3 64"/>
        <path id="arc-f" d="M 959.7 64 A 31 31 0 1 1 1012.3 64"/>
      </defs>

      <g role="img" aria-label="NZ sourced ingredients badge with fern emblem">
        <circle class="badge-ring" cx="68" cy="180" r="26"/><circle class="badge-inner" cx="68" cy="180" r="22"/>
        <text class="badge-caption badge-caption--light"><textPath href="#arc-a" startOffset="50%" text-anchor="middle">NZ SOURCED INGREDIENTS</textPath></text>
      </g>
      <g role="img" aria-label="Not tested on animals badge with rabbit emblem">
        <circle class="badge-ring" cx="153" cy="180" r="26"/><circle class="badge-inner" cx="153" cy="180" r="22"/>
        <text class="badge-caption badge-caption--light"><textPath href="#arc-b" startOffset="50%" text-anchor="middle">NOT TESTED ON ANIMALS</textPath></text>
      </g>
      <g role="img" aria-label="Made in New Zealand badge with mountain and fern emblem">
        <circle class="badge-ring" cx="237" cy="180" r="26"/><circle class="badge-inner" cx="237" cy="180" r="22"/>
        <text class="badge-caption badge-caption--light"><textPath href="#arc-c" startOffset="50%" text-anchor="middle">MADE IN NEW ZEALAND</textPath></text>
      </g>

      <g role="img" aria-label="Hydrating badge with water drop emblem">
        <circle class="badge-ring" cx="852" cy="54" r="26"/><circle class="badge-inner" cx="852" cy="54" r="22"/>
        <text class="badge-caption badge-caption--dark"><textPath href="#arc-d" startOffset="50%" text-anchor="middle">HYDRATING</textPath></text>
      </g>
      <g role="img" aria-label="For all skin types badge">
        <circle class="badge-ring" cx="918" cy="54" r="26"/><circle class="badge-inner" cx="918" cy="54" r="22"/>
        <text class="badge-caption badge-caption--dark"><textPath href="#arc-e" startOffset="50%" text-anchor="middle">FOR ALL SKIN TYPES</textPath></text>
      </g>
      <g role="img" aria-label="Hand-made badge with open hand and heart emblem">
        <circle class="badge-ring" cx="986" cy="54" r="26"/><circle class="badge-inner" cx="986" cy="54" r="22"/>
        <text class="badge-caption badge-caption--dark"><textPath href="#arc-f" startOffset="50%" text-anchor="middle">HAND-MADE</textPath></text>
      </g>
    </svg>
  </div>
</body>
</html>
```